Fantasy book Stonewake website needs a redesign (Wordpress)

My book website at www.stonewakenovel.example needs a redesign. It was originally done in Wordpress, so I need someone familiar with that to help make the site more professional and clean looking. Right now it feels too busy.

Industry/Entity Type

It Professional

Requirements
Must have
• Clean lines, easy to read, easy to navigate.
Nice to have
• If there was an easy way for me to blog to the site so I can keep my fans in the know, that would be great.
Should not have
• No cursive script, no flowery overly busy look. I like a clean modern look of a professional author.

```html
<!DOCTYPE html>
<html lang="en">
<head>
<meta charset="utf-8">
<title>Stonewake – Oath of the Tidecaller, Book 1</title>
<link rel="stylesheet" href="https://fonts.googleapis.com/css2?family=Rosario:ital,wght@0,400;0,600;1,400&display=swap">
<style>
:root{
  --page:#1b1b1b;
  --panel:#262626;
  --panel-edge:#3a3a3a;
  --card:#161616;
  --card-edge:#2e2e2e;
  --text:#b9b9b9;
  --text-soft:#8c8c8c;
  --white:#f2f2f2;
  --salmon:#f08070;
  --orange:#f0a030;
  --nav:#151515;
  --link-blue:#5aa8e6;
}
*{margin:0;padding:0;box-sizing:border-box}
html,body{width:1000px;height:1200px;overflow:hidden}
body{
  position:relative;
  background:
    radial-gradient(ellipse 520px 260px at 500px 60px,rgba(170,40,60,.55),rgba(60,20,60,.25) 55%,transparent 80%),
    var(--page);
  font-family:"Rosario",sans-serif;color:var(--text);font-size:11px;
}
.abs{position:absolute}
.brand{left:0;width:1000px;top:0;text-align:center}
.brand-name{font-size:60px;letter-spacing:3px;color:var(--white);line-height:70px;font-weight:400;text-transform:uppercase}
.brand-sub{font-size:17px;color:var(--white);margin-top:-8px}
.nav{left:144px;top:86px;width:711px;height:36px;background:var(--nav);display:flex;box-shadow:0 2px 6px rgba(0,0,0,.6)}
.nav a{display:flex;align-items:center;justify-content:center;color:var(--white);text-decoration:none;font-size:11.5px;text-transform:uppercase;border-right:1px solid #2c2c2c}
.nav a:last-child{border-right:0}
.nav a.active{color:var(--orange)}
.hero{left:124px;top:122px;width:752px;height:302px;
  background:
   radial-gradient(ellipse 200px 200px at 180px 110px,rgba(220,90,40,.8),transparent 70%),
   radial-gradient(ellipse 240px 220px at 560px 120px,rgba(90,80,200,.8),transparent 70%),
   radial-gradient(ellipse 110px 140px at 370px 220px,rgba(200,150,110,.55),transparent 75%),
   linear-gradient(90deg,#2a1010,#6a2040 35%,#3a2a6a 70%,#1c1a30)}
.welcome-title{left:144px;top:276px;width:221px;height:38px;background:rgba(15,15,15,.92);color:#f3d9a0;font-size:18px;line-height:38px;padding-left:12px;text-transform:uppercase}
.welcome-text{left:144px;top:318px;width:294px;height:92px;background:rgba(15,15,15,.92);color:var(--white);font-size:10.5px;line-height:17.8px;padding:6px 12px 0 15px}
.welcome-text a{color:var(--orange);text-decoration:none}
.slider-btn{top:388px;width:20px;height:20px;border-radius:50%;background:#d8d8d8;display:flex;align-items:center;justify-content:center}
.panel{background:var(--panel);border:1px solid var(--panel-edge)}
.panel h2{font-weight:400;color:var(--salmon);font-size:19px}
.about{left:144px;top:426px;width:494px;height:584px}
.author-photo{left:10px;top:40px;width:116px;height:122px;border:3px solid #eee;background:linear-gradient(#b0b0b0,#6a6a6a)}
.about-text{left:136px;top:44px;width:352px;line-height:17.7px;color:var(--text)}
.divider{left:10px;top:184px;width:472px;height:1px;background:#363636}
.card{background:linear-gradient(#262626,var(--card));border:1px solid var(--card-edge);box-shadow:0 2px 4px rgba(0,0,0,.5)}
.post{left:10px;width:473px;height:108px}
.post-thumb{left:8px;top:8px;width:73px;height:92px;border:2px solid #eee}
.post h3{position:absolute;left:93px;top:10px;font-weight:400;font-size:12px;color:var(--white)}
.post p{position:absolute;left:93px;top:35px;width:370px;line-height:16.3px;color:#cfcfcf;text-align:justify}
.post .meta{position:absolute;left:93px;top:87px;color:var(--text-soft);word-spacing:2px}
.side{left:645px;width:210px;height:288px}
.side .intro{left:10px;top:44px;width:192px;line-height:15px;font-size:9.5px;text-align:justify;color:var(--text-soft)}
.quote-card{left:7px;width:196px;height:101px}
.quote-card p{position:absolute;left:16px;top:12px;width:168px;font-size:9.5px;line-height:14.8px;color:var(--text-soft);text-align:justify}
.quote-card .who{position:absolute;left:16px;top:76px;color:var(--white);font-size:10.5px;display:flex;align-items:center;gap:8px}
.stars{display:flex;gap:3px}
.star{width:13px;height:13px;border:1px solid #bbb;display:flex;align-items:center;justify-content:center}
.quote-card.comment p{font-style:italic}
.foot-h{color:var(--orange);font-size:12.5px}
.foot-list{list-style:none;line-height:20.8px;color:var(--text-soft);font-size:10.5px}
.foot-list li::before{content:"» ";color:#777}
.social{list-style:none;font-size:9.5px;color:var(--text-soft)}
.social li{display:flex;align-items:center;height:22.4px;gap:8px}
.social .sq{width:19px;height:19px;background:#d8d8d8}
.social b{font-weight:400;font-size:11px;margin-left:3px;color:var(--link-blue)}
.copyright{left:0;width:1000px;top:1168px;text-align:center;color:#cfcfcf;font-size:10.5px;word-spacing:2px}
.copyright span{color:var(--text-soft)}
</style>
</head>
<body>
<header class="abs brand">
  <div class="brand-name">Stonewake</div>
  <div class="brand-sub">Oath of the Tidecaller, Book 1</div>
</header>

<nav class="abs nav">
  <a class="active" href="#" style="width:132px">Featured Artwork</a>
  <a href="#" style="width:112px">Featured Posts</a>
  <a href="#" style="width:52px">Links</a>
  <a href="#" style="width:138px">Opinions &amp; Concepts</a>
  <a href="#" style="width:122px">Preview the Book</a>
  <a href="#" style="width:74px">Reviews!</a>
  <a href="#" style="width:81px">Who am I?</a>
</nav>

<div class="abs hero" role="img" aria-label="Painted fantasy cover art: two armoured sorcerers in fiery red and violet light above a young blond hero"></div>
<div class="abs welcome-title">Welcome to Stonewake</div>
<div class="abs welcome-text">I want to thank everyone for their help and support in launch-ing my first two part novel, Stonewake, Oath of the Tidecaller. It’s been an amazing road, and you are my biggest motivation to write, for joy comes from sharing. <a href="#">More »</a></div>
<div class="abs slider-btn" style="left:808px"><svg width="8" height="10" viewBox="0 0 8 10"><path d="M6 1 2 5l4 4" stroke="#333" stroke-width="2" fill="none"/></svg></div>
<div class="abs slider-btn" style="left:834px"><svg width="8" height="10" viewBox="0 0 8 10"><path d="M2 1l4 4-4 4" stroke="#333" stroke-width="2" fill="none"/></svg></div>

<section class="abs panel about">
  <h2 class="abs" style="left:10px;top:8px">About Author</h2>
  <div class="abs author-photo" role="img" aria-label="Black and white portrait photo of the author"></div>
  <p class="abs about-text">The novel started out as a simple story about a small band of mages, but turned into the first part of an epic tale of assassins, dragons, and an adventure spanning millennia. I know I’ll need at least six books to tell this tale, maybe more! When I started writing, I thought I knew what was going to happen. As it turns out, I was mostly wrong. The story became deeper, my characters matured. Along the way some died, and others became pivotal in ways I could not have foreseen. I’d like to say I had it all planned, (I do for the sequels!)</p>
  <div class="abs divider"></div>
  <h2 class="abs" style="left:10px;top:196px;font-size:17px">Recent Posts</h2>
  <div class="abs slider-btn" style="left:469px;top:200px;width:14px;height:14px;background:#666"><svg width="6" height="8" viewBox="0 0 6 8"><path d="M1 1l3 3-3 3" stroke="#eee" stroke-width="1.6" fill="none"/></svg></div>

  <article class="abs card post" style="top:232px">
    <div class="abs post-thumb" style="background:#f4f4f4" role="img" aria-label="Scanned editor's letter"></div>
    <h3>Editor’s endorsement!</h3>
    <p>I just received my editor’s endorsement of Stonewake. Now the hard part (editing) starts, but I think the end result will be a better story. Looking forward to launching this book soon, and thank you all for your patience.</p>
    <div class="meta">November 22, 2012 &nbsp;admin &nbsp;(5) comments</div>
  </article>
  <article class="abs card post" style="top:350px">
    <div class="abs post-thumb" style="background:linear-gradient(90deg,#b04a30,#4a4aa0 50%,#b04a30 50%,#4a4aa0)" role="img" aria-label="Two book covers side by side"></div>
    <h3>Editor’s endorsement!</h3>
    <p>I just received my editor’s endorsement of Stonewake. Now the hard part (editing) starts, but I think the end result will be a better story. Looking forward to launching this book soon, and thank you all for your patience.</p>
    <div class="meta">November 22, 2012 &nbsp;admin &nbsp;(5) comments</div>
  </article>
  <article class="abs card post" style="top:468px">
    <div class="abs post-thumb" style="background:linear-gradient(135deg,#d06030,#7a4ab0)" role="img" aria-label="Cover art of an armoured hero with a sword"></div>
    <h3>Editor’s endorsement!</h3>
    <p>I just received my editor’s endorsement of Stonewake. Now the hard part (editing) starts, but I think the end result will be a better story. Looking forward to launching this book soon, and thank you all for your patience.</p>
    <div class="meta">November 22, 2012 &nbsp;admin &nbsp;(5) comments</div>
  </article>
</section>

<aside class="abs panel side" style="top:426px">
  <h2 class="abs" style="left:10px;top:10px;font-size:17px">Reviews</h2>
  <p class="abs intro">Cum sociis natoque penatibus et magnis dis parturient montes, nascetur ridiculus mus.</p>
  <div class="abs card quote-card" style="top:72px">
    <p>Cum sociis natoque penatibus et magnis dis parturient montes, nascetur ridiculus mus. Nullam ultrices hendrerit ante, vitae mollis risus tempor vitae.</p>
    <div class="who">Ada Lowell, NY <span class="stars"><i class="star"><svg width="9" height="9" viewBox="0 0 10 10"><path d="M5 0l1.5 3.3 3.5.3-2.7 2.3.9 3.6L5 7.6 1.8 9.5l.9-3.6L0 3.6l3.5-.3z" fill="#ddd"/></svg></i><i class="star"><svg width="9" height="9" viewBox="0 0 10 10"><path d="M5 0l1.5 3.3 3.5.3-2.7 2.3.9 3.6L5 7.6 1.8 9.5l.9-3.6L0 3.6l3.5-.3z" fill="#ddd"/></svg></i><i class="star"><svg width="9" height="9" viewBox="0 0 10 10"><path d="M5 0l1.5 3.3 3.5.3-2.7 2.3.9 3.6L5 7.6 1.8 9.5l.9-3.6L0 3.6l3.5-.3z" fill="#ddd"/></svg></i><i class="star"><svg width="9" height="9" viewBox="0 0 10 10"><path d="M5 0l1.5 3.3 3.5.3-2.7 2.3.9 3.6L5 7.6 1.8 9.5l.9-3.6L0 3.6l3.5-.3z" fill="#ddd"/></svg></i><i class="star" style="background:#888"></i></span></div>
  </div>
  <div class="abs card quote-card" style="top:180px">
    <p>Cum sociis natoque penatibus et magnis dis parturient montes, nascetur ridiculus mus. Nullam ultrices hendrerit ante, vitae mollis risus tempor vitae.</p>
    <div class="who">Ada Lowell, NY <span class="stars"><i class="star"><svg width="9" height="9" viewBox="0 0 10 10"><path d="M5 0l1.5 3.3 3.5.3-2.7 2.3.9 3.6L5 7.6 1.8 9.5l.9-3.6L0 3.6l3.5-.3z" fill="#ddd"/></svg></i><i class="star"><svg width="9" height="9" viewBox="0 0 10 10"><path d="M5 0l1.5 3.3 3.5.3-2.7 2.3.9 3.6L5 7.6 1.8 9.5l.9-3.6L0 3.6l3.5-.3z" fill="#ddd"/></svg></i><i class="star"><svg width="9" height="9" viewBox="0 0 10 10"><path d="M5 0l1.5 3.3 3.5.3-2.7 2.3.9 3.6L5 7.6 1.8 9.5l.9-3.6L0 3.6l3.5-.3z" fill="#ddd"/></svg></i><i class="star"><svg width="9" height="9" viewBox="0 0 10 10"><path d="M5 0l1.5 3.3 3.5.3-2.7 2.3.9 3.6L5 7.6 1.8 9.5l.9-3.6L0 3.6l3.5-.3z" fill="#ddd"/></svg></i><i class="star" style="background:#888"></i></span></div>
  </div>
</aside>

<aside class="abs panel side" style="top:722px">
  <h2 class="abs" style="left:10px;top:10px;font-size:17px">Recent comments</h2>
  <p class="abs intro">Cum sociis natoque penatibus et magnis dis parturient montes, nascetur ridiculus mus.</p>
  <div class="abs card quote-card comment" style="top:74px">
    <p><b style="color:#777;font-size:14px">“</b> &nbsp;Cum sociis natoque penatibus et magnis dis parturient montes, nascetur ridiculus mus. Nullam ultrices hendrerit ante, vitae mollis risus. <b style="color:#aaa;font-size:14px">”</b></p>
    <div class="who">Ada Lowell, NY</div>
  </div>
  <div class="abs card quote-card comment" style="top:181px">
    <p><b style="color:#777;font-size:14px">“</b> &nbsp;Cum sociis natoque penatibus et magnis dis parturient montes, nascetur ridiculus mus. Nullam ultrices hendrerit ante, vitae mollis risus. <b style="color:#aaa;font-size:14px">”</b></p>
    <div class="who">Ada Lowell, NY</div>
  </div>
</aside>

<footer>
  <div class="abs foot-h" style="left:158px;top:1027px">Archive</div>
  <ul class="abs foot-list" style="left:158px;top:1047px"><li>May 2013</li><li>November 2012</li><li>May 2012</li><li>April 2012</li></ul>
  <ul class="abs foot-list" style="left:262px;top:1048px"><li>March 2012</li><li>February 2012</li><li>January 2012</li></ul>
  <div class="abs foot-h" style="left:398px;top:1027px">Blog</div>
  <ul class="abs foot-list" style="left:398px;top:1047px"><li>Sed sollicitudin nibh fermentum orci</li><li>Mauris vehicula posuere sapien, vitae elementum</li><li>Donec bibendum tristique ante, vitae viverra quam</li><li>Etiam mauris sem, tempor sed</li></ul>
  <div class="abs foot-h" style="left:683px;top:1027px">Connect with us</div>
  <ul class="abs social" style="left:683px;top:1046px">
    <li><i class="sq"></i>Join with us on <b>Gatherly</b></li>
    <li><i class="sq"></i>Follow us on <b>Chirpline</b></li>
    <li><i class="sq"></i>Share on <b>Proflink</b></li>
    <li><i class="sq"></i>Watch on <b>Reelhouse</b></li>
  </ul>
  <div class="abs copyright">Copyright &nbsp;© &nbsp;2013 &nbsp;Stonewake. &nbsp;&nbsp;All rights reserved. &nbsp;&nbsp;&nbsp;<span>Privacy Policy &nbsp;| &nbsp;Terms and conditions</span></div>
</footer>
</body>
</html>
```